Hollow Lantern Double Sided Flyer Design

We need a double sided flyer (1/3 of an A4 which is 99mm x 210mm) developed for our Newcastle(NSW) tour. This flyer will be placed in tourist information centres and hotels. We want it to direct people to our website or be able to make bookings over the phone.

About Us:-
We are a city walking tour company that runs tours day or night. We run both day and night and will incorporate real history / real Hollow lantern. Some of the stories will be quite serious i.e.- there are infamous murders from 100 years ago, baffling court cases, even a bit of poetry written by murderers, suicides, love triangles, you name it. We will be telling the historical stories that tourists will not hear from any other tour provider. A bit of darkness, a bit of mystery and a bit of history theme.

We do no go for scares and let the very real stories deliver the entertainment for our guests. Our customers enjoy our tours, but it isn't light fun and frivolity. Our stories are being carefully crafted and are packed with unexpected twists, turns; revelations whilst remaining all 100% true. We deliver deep, rich, engaging stories.

Here are a few samples of quotes from the characters in our stories that may give you an idea of the kind of history we will cover:-

"There were bits of spines, bits of skulls, [and] finger bones spilled out all over the streets - I ended up filling three boxes. Children were playing with them for weeks”

"I had a close shave last night and now I want a close haircut.”

“She's a beautiful child', isn't she? She's the cause of all the trouble.”

“I did it because she would not come home with me.”

"I have killed my wife. I’m glad she’s dead.”

"Stand aside or I'll put a bullet through both of you."

“You villain, I'll teach you to take away my character."

“You’re not dead yet, you bastard!”

Our website, booking form and contact details can be viewed at www.hollowlantern-tours.com.au

Target Market(s)

Tourists

Industry/Entity Type

Tour

Colors

Designer to choose colors to be used in the design.

Requirements
Must have
• Vertical orientation please.
• Please also include a reference to a discount offer of 25% using the promo code "DARK".
Nice to have
• FRONT FLYER INFORMATION
• - Hollow Lantern Logo
• - "I have killed my wife; I'm glad she's dead."
• - Harbourside Buried Past Walk
• - 25% Discount Offer Codeword DARK
• - web address at the base; www.hollowlantern-tours.com.au
• BACK FLYER INFORMATION
• - "She's a beautiful child', isn't she? She's the cause of all the trouble.
• - Hollow Lantern Logo at the base along with the web address www.hollowlantern-tours.com.au
• - Blurb:- Hollow lantern brings back Newcastle's hidden past, the forgotten past, the dark past that may not want to be remembered.
• Real stories from the streets around you. Discover the histories you won't hear anywhere else. The forgotten stories of yesteryear finally get a chance to be told. Through you they get to live again.
Should not have
• GENERAL
• Please do not include the phone number, email address or social media icons. We want to drive online bookings.

```html
<!DOCTYPE html>
<html lang="en">
<head>
<meta charset="utf-8">
<title>Hollow Lantern Flyer – Front and Back</title>
<link href="https://fonts.googleapis.com/css2?family=Montserrat:wght@400;500;700;800&family=Rajdhani:wght@500;700&display=swap" rel="stylesheet">
<style>
  :root{
    --stage:#ececec;
    --red:#e8232b;
    --ink:#1f1f1f;
    --charcoal:#262626;
    --white:#ffffff;
    --grey-text:#333333;
  }
  *{box-sizing:border-box;margin:0;padding:0}
  html,body{width:1200px;height:1177px;overflow:hidden}
  body{background:var(--stage);position:relative;font-family:"Montserrat",sans-serif}

  .flyer{position:absolute;top:62px;width:490px;height:1039px;overflow:hidden;background:var(--charcoal)}
  .flyer--front{left:66px}
  .flyer--back{left:629px;background:var(--white)}

  .side-label{position:absolute;font-size:24px;color:var(--ink);transform:rotate(-90deg);transform-origin:left top;letter-spacing:1px}
  .side-label--front{left:566px;top:1097px}
  .side-label--back{left:1130px;top:1097px}

  .scene{position:absolute;left:0;width:100%}
  .scene--street{top:0;height:220px;background:linear-gradient(160deg,#6a6a6a 0%,#3b3b3b 55%,#1e1e1e 100%)}
  .scene--tram{top:220px;height:239px;background:linear-gradient(180deg,#9a9a9a 0%,#5a5a5a 45%,#2a2a2a 100%)}
  .scene--rail{top:459px;height:199px;background:linear-gradient(180deg,#3a3a3a 0%,#2a2a2a 60%,#1c1c1c 100%)}
  .scene--skyline{top:442px;height:216px;background:linear-gradient(180deg,#ffffff 0%,#dcdcdc 35%,#cfcfcf 70%,#e4e4e4 100%)}

  .quote{position:absolute;left:60px;right:10px;text-align:center;color:var(--white);font-size:17px;line-height:23px;font-weight:400}
  .quote--one{top:97px}
  .quote--two{top:376px}
  .quote--three{top:533px}
  .quote--back{left:60px;right:20px;top:530px;color:var(--ink);font-weight:700;font-size:19px;line-height:27px}

  .book-tab{position:absolute;left:0;width:52px;background:var(--red);border-radius:0 10px 10px 0;display:flex;align-items:center;justify-content:center}
  .book-tab span{transform:rotate(-90deg);white-space:nowrap;color:var(--white);font-weight:800;font-size:17px;letter-spacing:.5px}
  .book-tab--dark{background:#2b2b2b}
  .book-tab--dark span{color:var(--red)}

  .brand-band{position:absolute;left:0;top:658px;width:100%;height:152px;background:var(--red)}
  .brand-disc{position:absolute;left:131px;top:620px;width:228px;height:228px;border-radius:50%;background:var(--red)}
  .brand-name{position:absolute;left:0;right:0;top:747px;text-align:center;color:var(--white);font-weight:700;font-size:30px;letter-spacing:1px}

  .booking{position:absolute;left:0;top:810px;width:100%;height:229px;background:linear-gradient(180deg,#2c2c2c,#1f1f1f)}
  .booking__label{position:absolute;left:18px;top:33px;color:var(--white);font-size:19px}
  .booking__offer{position:absolute;left:16px;top:64px;font-family:"Rajdhani",sans-serif;font-weight:700;font-size:66px;line-height:66px;color:var(--red);letter-spacing:1px}
  .booking__web{position:absolute;left:18px;right:12px;top:133px;display:flex;align-items:center;gap:8px;font-family:"Rajdhani",sans-serif;font-weight:500;font-size:20px;color:var(--white);white-space:nowrap}
  .booking__web svg{flex:none}
  .booking__code{position:absolute;left:0;right:0;top:190px;text-align:center;color:var(--white);font-size:14.5px}
  .booking__code strong{color:var(--red);font-weight:800}

  .welcome{position:absolute;left:0;right:0;top:22px;text-align:center;color:var(--ink);font-size:37px;font-weight:400;letter-spacing:1px}
  .welcome__title{position:absolute;left:0;right:0;top:64px;text-align:center;color:var(--red);font-size:42px;font-weight:800}
  .welcome__rule{position:absolute;left:209px;top:128px;width:74px;height:2px;background:var(--red)}
  .blurb{position:absolute;left:32px;width:423px;top:145px;font-size:14.8px;line-height:19.2px;color:var(--grey-text);text-align:justify}
  .blurb p+p{margin-top:10px}
</style>
</head>
<body>

<section class="flyer flyer--front" aria-label="Flyer front">
  <div class="scene scene--street" role="img" aria-label="Black and white photo of an old city street with stone buildings"></div>
  <div class="scene scene--tram" role="img" aria-label="Black and white photo of a tram on a rainy street"></div>
  <div class="scene scene--rail" role="img" aria-label="Black and white photo of a steam train in a railway yard"></div>

  <div class="book-tab" style="top:32px;height:160px"><span>BOOK NOW!</span></div>
  <div class="book-tab" style="top:260px;height:160px"><span>BOOK NOW!</span></div>
  <div class="book-tab" style="top:472px;height:160px"><span>BOOK NOW!</span></div>

  <p class="quote quote--one">I have killed my wife.<br>I’m glad she’s dead.</p>
  <p class="quote quote--two">You villain,<br>I'll teach you to take away my character.</p>
  <p class="quote quote--three">I did it because<br>she would not come home with me.</p>

  <div class="brand-band"></div>
  <div class="booking">
    <p class="booking__label">Book online &amp; save :</p>
    <p class="booking__offer">25% OFF</p>
    <p class="booking__web">
      <svg width="18" height="18" viewBox="0 0 16 16"><circle cx="8" cy="8" r="8" fill="#e8232b"/><circle cx="8" cy="8" r="4.5" fill="none" stroke="#fff" stroke-width="1"/><path d="M3.5 8h9M8 3.5v9" stroke="#fff" stroke-width="1"/></svg>
      www.hollowlantern-tours.com.au
    </p>
    <p class="booking__code">Use promo code <strong>DARK</strong> when you book</p>
  </div>
  <div class="brand-disc"></div>
  <p class="brand-name">HOLLOW LANTERN</p>
</section>
<p class="side-label side-label--front">FRONT</p>

<section class="flyer flyer--back" aria-label="Flyer back">
  <h1 class="welcome">WELCOME TO</h1>
  <h2 class="welcome__title">HOLLOW LANTERN</h2>
  <div class="welcome__rule"></div>
  <div class="blurb">
    <p>Dark; a euphemism for the unknown or the forgotten..... the dark ages, dark matter, dark energy; things where knowledge is uncertain or unknown are dark. Hollow lantern brings back the hidden past, the forgotten past, the past that may not want to be remembered......but these are real stories....real stories that come from the streets around you.</p>
    <p>Some of these stories may be tales of dark things .....some may simply be a charming reminder of days gone by.....these stories are compelling reminders of the amazing times that precede us.....and the forgotten people of yesteryear finally get a chance to have their story told. Through you, the often dark lives of the people of yesterday get to live again. Will you like what you hear?</p>
  </div>
  <div class="scene scene--skyline" role="img" aria-label="Faded photo of a historic city skyline with a cathedral and clock tower"></div>
  <div class="book-tab book-tab--dark" style="top:483px;height:159px"><span>BOOK NOW!</span></div>
  <p class="quote quote--back">She's a beautiful child', isn't she?<br>She's the cause of all the trouble.</p>

  <div class="brand-band"></div>
  <div class="booking">
    <p class="booking__label">Book online &amp; save :</p>
    <p class="booking__offer">25% OFF</p>
    <p class="booking__web">
      <svg width="18" height="18" viewBox="0 0 16 16"><circle cx="8" cy="8" r="8" fill="#e8232b"/><circle cx="8" cy="8" r="4.5" fill="none" stroke="#fff" stroke-width="1"/><path d="M3.5 8h9M8 3.5v9" stroke="#fff" stroke-width="1"/></svg>
      www.hollowlantern-tours.com.au
    </p>
    <p class="booking__code">Use promo code <strong>DARK</strong> when you book</p>
  </div>
  <div class="brand-disc"></div>
  <p class="brand-name">HOLLOW LANTERN</p>
</section>
<p class="side-label side-label--back">BACK</p>

</body>
</html>
```